Service business needs Business Card Design

Looking to create a new business card design that is both professional and unique the can highlight the many services we offer throughout the seasons. Our tagline is "The Steadfast Touch"
Licensed & Insured: PA392617 has to be small and on the back side of the card.
On the Front:
FirstName LastName
Title
We offer the following services:
Deck Repair and Maintenance
Deck Cleaning and Staining/Painting
Power Washing/House Washing
Landscape Lighting Installation
Christmas Lighting Installation

```html
<!DOCTYPE html>
<html lang="en">
<head>
<meta charset="utf-8">
<title>Harbor Line Services – Business Card</title>
<link href="https://fonts.googleapis.com/css2?family=Montserrat:ital,wght@0,400;0,500;0,700;1,400&display=swap" rel="stylesheet">
<style>
  :root {
    --navy: #0b3563;
    --brand-blue: #0a4d8c;
    --sky: #44b2e2;
    --white: #ffffff;
    --frame: #222a33;
    --page: #ffffff;
  }
  * { box-sizing: border-box; margin: 0; padding: 0; }
  html, body { width: 1200px; height: 980px; overflow: hidden; background: var(--page); }
  body { font-family: "Montserrat", Arial, sans-serif; position: relative; }

  .sheet {
    position: absolute; inset: 0;
    border: 1px solid var(--frame);
  }

  .card {
    position: absolute; left: 330px; width: 540px; height: 330px;
    border: 1px solid var(--frame);
    overflow: hidden;
  }
  .card--front { top: 123px; background: var(--white); }
  .card--back { top: 527px; background: var(--white); }

  /* Wordmark */
  .brand-name {
    position: absolute; left: 0; right: 0; text-align: center;
    font-weight: 700; color: var(--brand-blue); white-space: nowrap;
  }
  .card--front .brand-name__main {
    top: 126px; font-size: 34px; letter-spacing: 3px; line-height: 40px;
  }
  .card--front .brand-name__sub {
    top: 164px; font-size: 11px; letter-spacing: 17px; padding-left: 17px; line-height: 14px;
  }

  /* Front */
  .divider {
    position: absolute; left: 84px; width: 371px; top: 208px;
    height: 2px; background: var(--navy);
  }
  .person { position: absolute; left: 63px; top: 233px; color: var(--navy); }
  .person__name { font-weight: 700; font-size: 17px; letter-spacing: 0.3px; }
  .person__title { font-style: italic; font-size: 17px; margin-top: 5px; letter-spacing: 0.5px; }
  .tagline {
    position: absolute; left: 350px; top: 233px; width: 150px;
    color: var(--navy); font-weight: 700; font-size: 16px; line-height: 22px;
    text-transform: uppercase; letter-spacing: 0.3px;
  }

  /* Back */
  .back-panel {
    position: absolute; left: 0; top: 0; width: 100%; height: 295px;
    background: var(--sky);
  }
  .card--back .brand-name { color: var(--white); left: 364px; right: auto; width: 170px; }
  .card--back .brand-name__main { top: 78px; font-size: 15px; letter-spacing: 1.5px; line-height: 18px; }
  .card--back .brand-name__sub { top: 99px; font-size: 7px; letter-spacing: 8px; padding-left: 8px; line-height: 9px; }

  .services { position: absolute; left: 48px; top: 131px; color: var(--white); }
  .services__heading { font-weight: 700; font-size: 20px; margin-bottom: 4px; }
  .services__list { list-style: none; }
  .services__item {
    position: relative; padding-left: 24px;
    font-size: 14px; line-height: 19.5px; letter-spacing: 0.3px;
  }
  .services__item::before {
    content: ""; position: absolute; left: 2px; top: 9px;
    width: 3px; height: 3px; border-radius: 50%; background: var(--white);
  }
  .license {
    position: absolute; left: 0; right: 0; top: 305px; text-align: center;
    color: var(--navy); font-weight: 700; font-size: 11px; letter-spacing: 5px;
  }
</style>
</head>
<body>
<div class="sheet">

  <section class="card card--front">
    <div class="brand-name brand-name__main">HARBOR LINE</div>
    <div class="brand-name brand-name__sub">SERVICES</div>
    <div class="divider"></div>
    <div class="person">
      <p class="person__name">FIRSTNAME LASTNAME</p>
      <p class="person__title">TITLE</p>
    </div>
    <p class="tagline">The Steadfast Touch</p>
  </section>

  <section class="card card--back">
    <div class="back-panel"></div>
    <div class="brand-name brand-name__main">HARBOR LINE</div>
    <div class="brand-name brand-name__sub">SERVICES</div>
    <div class="services">
      <h2 class="services__heading">Our Services</h2>
      <ul class="services__list">
        <li class="services__item">Deck Repair and Maintenance</li>
        <li class="services__item">Deck Cleaning and Staining/Painting</li>
        <li class="services__item">Power Washing/House Washing</li>
        <li class="services__item">Landscape Lighting Installation</li>
        <li class="services__item">Christmas Lighting Installation</li>
      </ul>
    </div>
    <p class="license">LICENSED &amp; INSURED: PA392617</p>
  </section>

</div>
</body>
</html>
```